Security doors and flyscreens

We need business cards for our company called K & M Distributors. We quote, manufacture and install security doors and flyscreens.

Industry/Entity Type

Security

Contact Information for Business Card

K & M DISTRIBUTORS
17 Larkvale Rd. Brindlewood 3189
Ph: 8157 2604
Fax: 8157 2609
Gavin: 0419 275 916
Email: gatesupplier@mailbox-example.net

```html
<!DOCTYPE html>
<html lang="en">
<head>
<meta charset="utf-8">
<title>K &amp; M Distributors – Business Card</title>
<link rel="stylesheet" href="https://fonts.googleapis.com/css2?family=Russo+One&family=Questrial&display=swap">
<style>
  :root {
    --backdrop: #4a4a4a;
    --card-white: #ffffff;
    --navy: #2b2d4e;
    --ink: #111111;
    --steel-light: #c9cbce;
    --steel-mid: #8d9094;
    --steel-dark: #55585c;
  }
  html, body {
    margin: 0;
    padding: 0;
    width: 1200px;
    height: 905px;
    overflow: hidden;
    background: var(--backdrop);
  }
  .business-card {
    position: absolute;
    left: 180px;
    top: 212px;
    width: 840px;
    height: 480px;
    background: var(--card-white);
    overflow: hidden;
    box-shadow: 0 10px 30px rgba(0,0,0,0.35);
  }
  .card-shapes {
    position: absolute;
    inset: 0;
  }
  .company-name {
    position: absolute;
    right: 40px;
    top: 34px;
    margin: 0;
    font-family: "Russo One", sans-serif;
    font-weight: 400;
    font-size: 44px;
    letter-spacing: 1px;
    color: var(--ink);
    white-space: nowrap;
  }
  .tagline {
    position: absolute;
    right: 40px;
    top: 96px;
    margin: 0;
    text-align: right;
    font-family: "Questrial", sans-serif;
    font-size: 25px;
    line-height: 1.15;
    color: var(--ink);
  }
  .contact-details {
    position: absolute;
    right: 40px;
    top: 222px;
    margin: 0;
    text-align: right;
    font-family: "Questrial", sans-serif;
    font-style: normal;
    font-size: 25px;
    line-height: 1.2;
    color: var(--card-white);
    white-space: nowrap;
  }
  .brand-mark {
    position: absolute;
    left: 40px;
    top: 228px;
    display: flex;
    align-items: center;
    gap: 10px;
    font-family: "Russo One", sans-serif;
    font-size: 30px;
    color: var(--navy);
  }
  .brand-mark .dot {
    width: 22px;
    height: 22px;
    border-radius: 50%;
    background: var(--navy);
  }
</style>
</head>
<body>
  <section class="business-card">
    <svg class="card-shapes" width="840" height="480" viewBox="0 0 840 480">
      <defs>
        <linearGradient id="steel" x1="0" y1="0" x2="1" y2="1">
          <stop offset="0" stop-color="#55585c"/>
          <stop offset="0.45" stop-color="#c9cbce"/>
          <stop offset="1" stop-color="#8d9094"/>
        </linearGradient>
      </defs>
      <polygon class="door-photo" role="img" aria-label="Close-up photo of a steel security door corner with perforated mesh panel"
               points="0,0 150,0 330,180 250,480 0,480" fill="url(#steel)"/>
      <polygon class="navy-band" points="330,180 840,180 840,480 250,480" fill="#2b2d4e"/>
    </svg>

    <div class="brand-mark"><span class="dot"></span>K &amp; M</div>

    <h1 class="company-name">K &amp; M DISTRIBUTORS</h1>
    <p class="tagline">Manufacturers &amp; Installers<br>Security Doors &amp; Flyscreens</p>

    <address class="contact-details">
      17 Larkvale Rd.<br>
      Brindlewood 3189<br>
      Ph: 8157 2604<br>
      Fax : 8157 2609<br>
      Mob: 0419 275 916<br>
      gatesupplier@mailbox-example.net
    </address>
  </section>
</body>
</html>
```